Modern Catering Company needs Letterhead Design

We need a letterhead design that will make effective use of the corporate logo and color scheme, along with careful typography, helps this letterhead design communicate the brand well. We do have a corporate logo, however feel free to enhance the color scheme with gold and purple. We are serving a very upscale clientele so the letterhead has to reflect elegance, professionalism, cleanliness, and modern style. We are branding the company so the letterhead and business cards must fit the brand story. There should be no cartoonish elements in the design and we are looking for sharper lines.

Target Market(s)

Businesses and upscale clientele

Industry/Entity Type

Catering

Contact Information for Business Card

while this design can have any number of quirks and distinctions, it needs to be cohesive with the entire brand story clean, professional but edgy

Requirements
Must have
• must have good and carefully placement of it’s logo and where you place the text or the message. Colors blue, very deep purple, jewel tones not pastels, gold. Blue must be the primary color you may accent with purple or gold. Contact information is as follows: Co-Owners/ Chefs: R. Hollowell & T. Brenn, phone: 414-555-0182 email:Contact@emberoakcatering.example, address: 6172 W Larkmoor Ln, Milwaukee, WI 53299
Should not have
• pastel colors, Do not add the BBQ information to the letterhead or business card it was a mistake by the previous designer.

```html
<!DOCTYPE html>
<html lang="en">
<head>
<meta charset="utf-8">
<title>Ember Oak Catering — Letterhead</title>
<link rel="stylesheet" href="https://fonts.googleapis.com/css2?family=Open+Sans:wght@600&display=swap">
<style>
  :root {
    --backdrop: #e6e7e8;
    --paper: #ffffff;
    --brand-blue: #3a63b8;
    --ink: #1f2226;
    --faint-mark: #eceef4;
  }
  * { margin: 0; padding: 0; box-sizing: border-box; }
  html, body {
    width: 1200px; height: 849px; overflow: hidden;
    background: var(--backdrop);
    font-family: "Open Sans", Arial, sans-serif;
  }
  .letterhead {
    position: absolute; left: 300px; top: 0;
    width: 600px; height: 849px;
    background: var(--paper);
  }
  .brand {
    position: absolute; left: 87px; top: 62px;
    display: flex; align-items: center; gap: 8px;
  }
  .brand-dot {
    width: 14px; height: 14px; border-radius: 50%;
    background: var(--brand-blue); flex: none;
  }
  .brand-name {
    color: var(--brand-blue); font-weight: 600;
    font-size: 22px; line-height: 1.15; letter-spacing: 0.5px;
    text-transform: uppercase;
  }
  .divider {
    position: absolute; left: 273px; top: 86px;
    width: 1.5px; height: 65px; background: var(--brand-blue);
  }
  .contact {
    position: absolute; left: 284px; top: 84px;
    color: var(--ink); font-weight: 600; font-size: 11.5px;
    line-height: 15px; letter-spacing: 0.3px; font-style: normal;
  }
  .contact-address { margin-left: 0; }
  .contact-line { display: flex; align-items: center; gap: 8px; margin-left: 0; }
  .contact-line:first-of-type { margin-top: 8px; }
  .contact-icon { width: 10px; height: 10px; flex: none; }
  .center-mark {
    position: absolute; left: 200px; top: 363px;
    width: 200px; height: 200px; border-radius: 50%;
    background: var(--faint-mark);
  }
</style>
</head>
<body>
  <main class="letterhead">
    <header>
      <div class="brand">
        <span class="brand-dot"></span>
        <span class="brand-name">Ember Oak<br>Catering</span>
      </div>
      <div class="divider"></div>
      <address class="contact">
        <div class="contact-address">6172 W Larkmoor Ln<br>Milwaukee, WI 53299</div>
        <div class="contact-line">
          <svg class="contact-icon" viewBox="0 0 10 10" aria-hidden="true">
            <path d="M2 0.8 L3.6 0.8 L4.2 3 L3 3.8 Q4 6 6.2 7 L7 5.8 L9.2 6.4 L9.2 8 Q9 9.2 7.8 9.2 Q1 8.6 0.8 2 Q0.8 0.8 2 0.8 Z" fill="var(--brand-blue)"/>
          </svg>
          <span>414-555-0182</span>
        </div>
        <div class="contact-line">
          <svg class="contact-icon" viewBox="0 0 10 10" aria-hidden="true">
            <rect x="0.7" y="2" width="8.6" height="6" fill="none" stroke="var(--brand-blue)" stroke-width="1"/>
            <path d="M0.7 2 L5 5.5 L9.3 2" fill="none" stroke="var(--brand-blue)" stroke-width="1"/>
          </svg>
          <span>Contact@emberoakcatering.example</span>
        </div>
      </address>
    </header>
    <div class="center-mark" role="img" aria-label="Faint brand emblem placed at the centre of the sheet"></div>
  </main>
</body>
</html>
```